quiet orchard

It is a small business that is looking to sell medical supplies and services. later down the line it will branch off to help solve other world problems, i.e. global warming and raw material shortages.
but we will start with hospital equipment and supplies.

Target Market(s)

all medical facilities

Coding

Coded - Design and coding required

Number of Pages Required

1 page

```html
<!DOCTYPE html>
<html lang="en">
<head>
<meta charset="utf-8">
<title>Quiet Orchard — Hospital Equipment and Supplies</title>
<link rel="stylesheet" href="https://fonts.googleapis.com/css2?family=Roboto:wght@400;500;700&display=swap">
<style>
:root{
  --navy:#0b3a6d;
  --navy-deep:#0a0d45;
  --cyan:#0aa8e8;
  --ink:#222a35;
  --muted:#8a8f96;
  --panel:#f2f2f2;
  --white:#ffffff;
  --line:#dcdcdc;
}
*{box-sizing:border-box;margin:0;padding:0}
html,body{width:1200px;height:3727px;overflow:hidden}
body{font-family:'Roboto',Arial,sans-serif;color:var(--ink);background:var(--white);position:relative}
.abs{position:absolute}
svg{display:block}

.site-header{position:absolute;left:0;top:0;width:1200px;height:98px;background:var(--navy)}
.brand{position:absolute;left:29px;top:32px;font-size:30px;font-weight:500;color:var(--white);letter-spacing:.2px}
.main-nav{position:absolute;left:525px;top:48px;display:flex;gap:30px;font-size:11.5px;font-weight:500;color:var(--white)}
.main-nav .active{color:var(--cyan)}
.header-icons{position:absolute;left:968px;top:40px;display:flex;gap:24px}
.cart-count{position:absolute;left:1132px;top:30px;width:18px;height:18px;border-radius:50%;background:var(--cyan);color:#fff;font-size:10px;text-align:center;line-height:18px}

.hero{position:absolute;left:0;top:98px;width:1200px;height:546px;background:linear-gradient(90deg,#8e9497 0%,#b7bcbe 45%,#d9dcdd 75%,#c3c7ca 100%);overflow:hidden}
.hero-title{position:absolute;left:97px;top:165px;font-size:52px;font-weight:700;color:var(--white);letter-spacing:.5px}
.hero-text{position:absolute;left:97px;top:242px;width:400px;font-size:17px;font-weight:500;line-height:22px;color:var(--white)}
.hero-btn{position:absolute;left:97px;top:310px;width:178px;height:58px;background:var(--navy);color:#fff;font-size:22px;font-weight:500;text-align:center;line-height:58px}

.section-title{position:absolute;left:0;width:1200px;text-align:center;font-size:33px;font-weight:700;color:var(--ink)}
.section-title.light{color:var(--white)}

.product-card{position:absolute;width:201px;height:314px;background:var(--white);box-shadow:0 0 8px rgba(0,0,0,.12)}
.product-photo{position:absolute;left:14px;top:24px;width:173px;height:150px;border-radius:6px;background:radial-gradient(circle at 50% 50%,#dfe5ea 0%,#f6f7f8 70%,#fff 100%)}
.price{position:absolute;left:0;top:202px;width:100%;text-align:center;font-size:15px;font-weight:700;color:var(--cyan)}
.pname{position:absolute;left:0;top:225px;width:100%;text-align:center;font-size:14px;color:var(--muted)}
.buy{position:absolute;left:42px;top:255px;display:flex;height:31px}
.buy .label{width:88px;border:1.5px solid #333;font-size:12px;font-weight:700;text-align:center;line-height:28px;color:#222}
.buy .cart{width:32px;border:1.5px solid var(--cyan);border-left:none;display:flex;align-items:center;justify-content:center}
.buy.hover .label{background:var(--cyan);border-color:var(--cyan);color:#fff}
.buy.hover .cart{background:var(--navy);border-color:var(--navy)}

.best-band{position:absolute;left:0;top:1222px;width:1200px;height:554px;background:var(--navy)}

.services{position:absolute;left:0;top:1776px;width:1200px;height:714px;background:var(--panel)}
.service{position:absolute;width:200px;text-align:center}
.service svg{margin:0 auto}
.service h3{font-size:22px;font-weight:400;line-height:27px;color:var(--ink);margin-top:26px}
.service p{font-size:12.5px;line-height:16px;color:var(--muted);margin-top:20px;white-space:nowrap}
.service-divider{position:absolute;left:139px;top:403px;width:920px;height:1px;background:var(--line)}

.blog-card{position:absolute;width:289px;height:412px;background:#fff;box-shadow:0 0 8px rgba(0,0,0,.12)}
.blog-photo{position:absolute;left:20px;top:21px;width:249px;height:184px;background:linear-gradient(135deg,#c8d6e2,#e9eef2 55%,#9fb3c4)}
.blog-date{position:absolute;left:67px;top:191px;width:116px;height:26px;background:var(--cyan);color:#fff;font-size:15px;font-weight:700;text-align:center;line-height:26px}
.blog-title{position:absolute;left:0;top:258px;width:289px;text-align:center;font-size:19.5px;font-weight:700;line-height:25px;color:var(--ink);white-space:nowrap}
.blog-text{position:absolute;left:0;top:317px;width:289px;text-align:center;font-size:12.5px;line-height:16.5px;color:var(--muted);white-space:nowrap}

.features{position:absolute;left:0;top:3105px;width:1200px;height:149px;background:var(--cyan)}
.feature{position:absolute;top:48px;display:flex;align-items:center;gap:14px;color:#fff;font-size:23px}

.site-footer{position:absolute;left:0;top:3254px;width:1200px;height:473px;background:var(--navy-deep)}
.footer-col{position:absolute;top:84px}
.footer-col h4{font-size:18px;font-weight:700;color:var(--cyan);margin-bottom:12px}
.footer-col li{list-style:none;font-size:14px;line-height:24.5px;color:#fff}
.social li{display:flex;align-items:center;gap:14px;line-height:32.5px}
.social .dot{width:15px;height:15px;border-radius:50%;border:2px solid #fff}
.footer-divider{position:absolute;top:80px;width:3px;height:238px;background:linear-gradient(var(--cyan) 0 40px,#24306b 40px)}
.footer-bottom{position:absolute;left:0;top:379px;width:1200px;height:94px;border-top:1px solid #161a55}
.copyright{position:absolute;left:139px;top:44px;font-size:13px;color:#fff}
.footer-brand{position:absolute;left:527px;top:33px;font-size:26px;font-weight:500;color:#fff}
.legal{position:absolute;top:44px;font-size:13px;color:#fff}
</style>
</head>
<body>

<header class="site-header">
  <div class="brand">Quiet Orchard</div>
  <nav class="main-nav">
    <span class="active">HOME</span><span>ABOUT</span><span>SHOP</span><span>HOSPITAL EQUIPMENT AND SUPPLIES</span>
  </nav>
  <div class="header-icons">
    <svg width="24" height="24" viewBox="0 0 24 24" fill="none" stroke="#fff" stroke-width="2"><circle cx="12" cy="8" r="4"/><path d="M4 21c0-4 4-6 8-6s8 2 8 6z"/></svg>
    <svg width="24" height="24" viewBox="0 0 24 24" fill="none" stroke="#fff" stroke-width="2.2"><circle cx="10" cy="10" r="7"/><path d="M15 15l6 6"/></svg>
    <svg width="24" height="24" viewBox="0 0 24 24" fill="none" stroke="#fff" stroke-width="2"><path d="M12 21s-8-5-8-11a4.5 4.5 0 018-3 4.5 4.5 0 018 3c0 6-8 11-8 11z"/></svg>
    <svg width="26" height="24" viewBox="0 0 26 24" fill="none" stroke="#fff" stroke-width="2"><path d="M1 3h4l3 12h13l3-9H7"/><circle cx="10" cy="20" r="1.8"/><circle cx="19" cy="20" r="1.8"/></svg>
  </div>
  <div class="cart-count">0</div>
</header>

<section class="hero">
  <div class="abs" role="img" aria-label="Patient vital signs monitor in a hospital room" style="left:470px;top:0;width:730px;height:546px;background:linear-gradient(100deg,rgba(238,240,241,0) 0%,#e6e9ea 25%,#cfd4d7 60%,#b5bbbf)"></div>
  <h1 class="hero-title">QUIET ORCHARD</h1>
  <p class="hero-text">Lorem ipsum dolor loremit amet consectetur adipiscing eliultriceslorem ispsu gravida.</p>
  <div class="hero-btn">SHOP NOW</div>
</section>

<h2 class="section-title" style="top:716px">TRENDING PRODUCTS</h2>

<div class="product-card" style="left:139px;top:803px">
  <div class="product-photo" role="img" aria-label="Digital blood pressure monitor"></div>
  <div class="price">$25.00</div><div class="pname">Product Name</div>
  <div class="buy"><span class="label">BUY NOW</span><span class="cart"><svg width="20" height="18" viewBox="0 0 26 24" fill="none" stroke="#0aa8e8" stroke-width="2.2"><path d="M1 3h4l3 12h13l3-9H7"/><circle cx="10" cy="20" r="1.8"/><circle cx="19" cy="20" r="1.8"/></svg></span></div>
</div>
<div class="product-card" style="left:378px;top:803px">
  <div class="product-photo" role="img" aria-label="MRI scanner"></div>
  <div class="price">$25.00</div><div class="pname">Product Name</div>
  <div class="buy"><span class="label">BUY NOW</span><span class="cart"><svg width="20" height="18" viewBox="0 0 26 24" fill="none" stroke="#0aa8e8" stroke-width="2.2"><path d="M1 3h4l3 12h13l3-9H7"/><circle cx="10" cy="20" r="1.8"/><circle cx="19" cy="20" r="1.8"/></svg></span></div>
</div>
<div class="product-card" style="left:617px;top:803px">
  <div class="product-photo" role="img" aria-label="Manual blood pressure cuff with gauge"></div>
  <div class="price">$25.00</div><div class="pname">Product Name</div>
  <div class="buy hover"><span class="label">BUY NOW</span><span class="cart"><svg width="20" height="18" viewBox="0 0 26 24" fill="none" stroke="#fff" stroke-width="2.2"><path d="M1 3h4l3 12h13l3-9H7"/><circle cx="10" cy="20" r="1.8"/><circle cx="19" cy="20" r="1.8"/></svg></span></div>
</div>
<div class="product-card" style="left:856px;top:803px">
  <div class="product-photo" role="img" aria-label="Disposable surgical face mask"></div>
  <div class="price">$25.00</div><div class="pname">Product Name</div>
  <div class="buy"><span class="label">BUY NOW</span><span class="cart"><svg width="20" height="18" viewBox="0 0 26 24" fill="none" stroke="#0aa8e8" stroke-width="2.2"><path d="M1 3h4l3 12h13l3-9H7"/><circle cx="10" cy="20" r="1.8"/><circle cx="19" cy="20" r="1.8"/></svg></span></div>
</div>

<section class="best-band">
  <h2 class="section-title light" style="top:66px">BEST SELLING PRODUCTS</h2>
</section>
<div class="product-card" style="left:140px;top:1371px">
  <div class="product-photo" role="img" aria-label="Set of surgical forceps and scissors"></div>
  <div class="price">$25.00</div><div class="pname">Product Name</div>
  <div class="buy"><span class="label">BUY NOW</span><span class="cart"><svg width="20" height="18" viewBox="0 0 26 24" fill="none" stroke="#0aa8e8" stroke-width="2.2"><path d="M1 3h4l3 12h13l3-9H7"/><circle cx="10" cy="20" r="1.8"/><circle cx="19" cy="20" r="1.8"/></svg></span></div>
</div>
<div class="product-card" style="left:380px;top:1371px">
  <div class="product-photo" role="img" aria-label="Ultrasound therapy device"></div>
  <div class="price">$25.00</div><div class="pname">Product Name</div>
  <div class="buy"><span class="label">BUY NOW</span><span class="cart"><svg width="20" height="18" viewBox="0 0 26 24" fill="none" stroke="#0aa8e8" stroke-width="2.2"><path d="M1 3h4l3 12h13l3-9H7"/><circle cx="10" cy="20" r="1.8"/><circle cx="19" cy="20" r="1.8"/></svg></span></div>
</div>
<div class="product-card" style="left:618px;top:1371px">
  <div class="product-photo" role="img" aria-label="Portable ultrasound scanner"></div>
  <div class="price">$25.00</div><div class="pname">Product Name</div>
  <div class="buy"><span class="label">BUY NOW</span><span class="cart"><svg width="20" height="18" viewBox="0 0 26 24" fill="none" stroke="#0aa8e8" stroke-width="2.2"><path d="M1 3h4l3 12h13l3-9H7"/><circle cx="10" cy="20" r="1.8"/><circle cx="19" cy="20" r="1.8"/></svg></span></div>
</div>
<div class="product-card" style="left:858px;top:1371px">
  <div class="product-photo" role="img" aria-label="Blue stethoscope"></div>
  <div class="price">$25.00</div><div class="pname">Product Name</div>
  <div class="buy"><span class="label">BUY NOW</span><span class="cart"><svg width="20" height="18" viewBox="0 0 26 24" fill="none" stroke="#0aa8e8" stroke-width="2.2"><path d="M1 3h4l3 12h13l3-9H7"/><circle cx="10" cy="20" r="1.8"/><circle cx="19" cy="20" r="1.8"/></svg></span></div>
</div>

<section class="services">
  <h2 class="section-title" style="top:54px;font-size:31px">MEDICAL SUPPLIES AND SERVICES</h2>

  <div class="service" style="left:129px;top:152px">
    <svg width="104" height="84" viewBox="0 0 104 84"><rect x="10" y="2" width="84" height="62" rx="5" fill="#0aa8e8"/><rect x="20" y="11" width="64" height="44" fill="#f2f2f2"/><path d="M46 18h12v10h10v12H58v10H46V40H36V28h10z" fill="#0aa8e8"/><rect x="0" y="68" width="104" height="12" rx="4" fill="#0aa8e8"/></svg>
    <h3>Diagnostic<br>equipment</h3>
    <p>Lorem ipsum dolor sit amet,<br>consectetur adipiscing elit do<br>eiusmod tempor incun.</p>
  </div>
  <div class="service" style="left:375px;top:152px">
    <svg width="96" height="84" viewBox="0 0 96 84"><path d="M48 2L2 42h12v40h68V42h12z" fill="#0aa8e8"/><path d="M48 14L22 37v38h52V37z" fill="#f2f2f2"/><path d="M42 42h12v10h10v12H54v10H42V64H32V52h10z" fill="#0aa8e8"/></svg>
    <h3>Medical<br>equipment</h3>
    <p>Lorem ipsum dolor sit amet,<br>consectetur adipiscing elit do<br>eiusmod tempor incun.</p>
  </div>
  <div class="service" style="left:621px;top:152px">
    <svg width="108" height="84" viewBox="0 0 108 84"><rect x="2" y="20" width="10" height="62" fill="#0aa8e8"/><circle cx="30" cy="38" r="11" fill="#0aa8e8"/><path d="M46 30h50a10 10 0 0110 10v42h-10V66H12V52h34z" fill="#0aa8e8"/></svg>
    <h3>Furniture<br>and Fittings</h3>
    <p>Lorem ipsum dolor sit amet,<br>consectetur adipiscing elit do<br>eiusmod tempor incun.</p>
  </div>
  <div class="service" style="left:867px;top:152px">
    <svg width="90" height="84" viewBox="0 0 90 84"><path d="M30 4h30v12h-8V10H38v6h-8z" fill="#0aa8e8"/><rect x="4" y="16" width="82" height="66" rx="6" fill="#0aa8e8"/><path d="M39 32h12v12h12v12H51v12H39V56H27V44h12z" fill="#f2f2f2"/></svg>
    <h3>Wound care</h3>
    <p style="margin-top:47px">Lorem ipsum dolor sit amet,<br>consectetur adipiscing elit do<br>eiusmod tempor incun.</p>
  </div>

  <div class="service-divider"></div>

  <div class="service" style="left:129px;top:427px">
    <svg width="70" height="84" viewBox="0 0 70 84"><rect x="18" y="2" width="22" height="10" fill="#0aa8e8"/><path d="M40 4h20v8H40z" fill="#0aa8e8"/><rect x="20" y="14" width="18" height="12" fill="#0aa8e8"/><rect x="10" y="28" width="40" height="54" rx="8" fill="#0aa8e8"/><path d="M25 44h10v9h9v10h-9v9H25v-9h-9V53h9z" fill="#f2f2f2"/></svg>
    <h3>Disposable</h3>
    <p style="margin-top:47px">Lorem ipsum dolor sit amet,<br>consectetur adipiscing elit do<br>eiusmod tempor incun.</p>
  </div>
  <div class="service" style="left:375px;top:427px">
    <svg width="80" height="84" viewBox="0 0 80 84"><rect x="2" y="4" width="76" height="52" fill="#0aa8e8"/><path d="M8 30h16l6-12 8 22 7-14 5 4h22" fill="none" stroke="#f2f2f2" stroke-width="4"/><rect x="2" y="60" width="76" height="22" fill="#0aa8e8"/><rect x="8" y="66" width="8" height="5" fill="#f2f2f2"/><rect x="20" y="66" width="8" height="5" fill="#f2f2f2"/></svg>
    <h3>General<br>Supplies</h3>
    <p>Lorem ipsum dolor sit amet,<br>consectetur adipiscing elit do<br>eiusmod tempor incun.</p>
  </div>
  <div class="service" style="left:621px;top:427px">
    <svg width="96" height="84" viewBox="0 0 96 84"><rect x="6" y="2" width="34" height="78" rx="17" fill="#0aa8e8"/><rect x="14" y="14" width="10" height="30" rx="5" fill="#f2f2f2"/><rect x="50" y="6" width="34" height="78" rx="17" transform="rotate(-40 67 45)" fill="#0aa8e8"/></svg>
    <h3>Medical<br>Supplies</h3>
    <p>Lorem ipsum dolor sit amet,<br>consectetur adipiscing elit do<br>eiusmod tempor incun.</p>
  </div>
  <div class="service" style="left:867px;top:427px">
    <svg width="80" height="84" viewBox="0 0 80 84"><path d="M22 30L72 78M22 54L72 6" stroke="#0aa8e8" stroke-width="12" stroke-linecap="round"/><circle cx="16" cy="18" r="12" fill="none" stroke="#0aa8e8" stroke-width="8"/><circle cx="16" cy="66" r="12" fill="none" stroke="#0aa8e8" stroke-width="8"/></svg>
    <h3>Surgical<br>instruments</h3>
    <p>Lorem ipsum dolor sit amet,<br>consectetur adipiscing elit do<br>eiusmod tempor incun.</p>
  </div>
</section>

<h2 class="section-title" style="top:2530px;font-size:31px">LATEST BLOG</h2>

<article class="blog-card" style="left:139px;top:2606px">
  <div class="blog-photo" role="img" aria-label="Doctor preparing a patient for an imaging scan"></div>
  <div class="blog-date">Dec 03 2021</div>
  <h3 class="blog-title">Lorem ipsum dolor sit<br>amet, consectetur</h3>
  <p class="blog-text">Lorem ipsum dolor sit amet, con<br>sectetur adipiscing elit, sed do eius<br>tempor incididunt ut labore et dolore<br>magna aliquapsum suspen</p>
</article>
<article class="blog-card" style="left:455px;top:2606px">
  <div class="blog-photo" role="img" aria-label="Laboratory technician working with lab equipment"></div>
  <div class="blog-date">Dec 03 2021</div>
  <h3 class="blog-title">Lorem ipsum dolor sit<br>amet, consectetur</h3>
  <p class="blog-text">Lorem ipsum dolor sit amet, con<br>sectetur adipiscing elit, sed do eius<br>tempor incididunt ut labore et dolore<br>magna aliquapsum suspen</p>
</article>
<article class="blog-card" style="left:767px;top:2606px">
  <div class="blog-photo" role="img" aria-label="Pulse oximeter and stethoscope on a desk"></div>
  <div class="blog-date">Dec 03 2021</div>
  <h3 class="blog-title">Lorem ipsum dolor sit<br>amet, consectetur</h3>
  <p class="blog-text">Lorem ipsum dolor sit amet, con<br>sectetur adipiscing elit, sed do eius<br>tempor incididunt ut labore et dolore<br>magna aliquapsum suspen</p>
</article>

<section class="features">
  <div class="feature" style="left:138px">
    <svg width="60" height="54" viewBox="0 0 60 54" fill="none" stroke="#fff" stroke-width="2.5"><path d="M18 4h40v36H18zM18 16H8L2 28v12h16"/><circle cx="12" cy="44" r="6" fill="#0aa8e8"/><circle cx="46" cy="44" r="6" fill="#0aa8e8"/></svg>
    <span>Free Shipping</span>
  </div>
  <div class="feature" style="left:442px">
    <svg width="44" height="50" viewBox="0 0 44 50" fill="none" stroke="#fff" stroke-width="3"><path d="M4 3l20 22L4 47M18 3l20 22-20 22"/></svg>
    <span>Next Day Delivery*</span>
  </div>
  <div class="feature" style="left:760px">
    <svg width="58" height="60" viewBox="0 0 58 60" fill="none" stroke="#fff" stroke-width="3"><path d="M8 32V26a21 21 0 0142 0v6"/><rect x="3" y="28" width="10" height="18" rx="4"/><rect x="45" y="28" width="10" height="18" rx="4"/><path d="M50 46c0 8-8 10-16 10"/><rect x="22" y="52" width="12" height="7" rx="3"/></svg>
    <span>Customer Service</span>
  </div>
</section>

<footer class="site-footer">
  <div class="footer-col" style="left:139px"><h4>SHOP</h4><ul><li>Equipment</li><li>Consumables</li><li>&nbsp;Pharmaceuticals</li><li>Product Index</li><li>Product Catalogue</li><li>Software Support</li><li>Supplies</li></ul></div>
  <div class="footer-divider" style="left:336px"></div>
  <div class="footer-col" style="left:402px"><h4>ABOUT</h4><ul><li>About Us</li><li>Social Responsibility</li><li>Partner Program</li><li>Affilorem sid</li><li>Sell your Product</li><li>Shop Location</li><li>Best Seller</li></ul></div>
  <div class="footer-divider" style="left:605px"></div>
  <div class="footer-col" style="left:694px"><h4>HELP</h4><ul><li>Delivery</li><li>Returns</li><li>Help Center</li><li>Guidelines</li><li>Copyright</li><li>Investor Center</li><li>Contact Us</li></ul></div>
  <div class="footer-divider" style="left:856px"></div>
  <div class="footer-col social" style="left:926px"><h4>SOCIAL</h4><ul><li><span class="dot"></span>Lenswall</li><li><span class="dot"></span>Townsquare</li><li><span class="dot"></span>Birdcall</li><li><span class="dot"></span>Shortpost</li><li><span class="dot"></span>Moodboard</li></ul></div>

  <div class="footer-bottom">
    <div class="copyright">© 2022 quiet orchard. All Rights Reserved</div>
    <div class="footer-brand">Quiet Orchard</div>
    <div class="legal" style="left:804px">Privacy Policy</div>
    <div class="legal" style="left:952px">Cookie Policy</div>
  </div>
</footer>

</body>
</html>
```